Bold Website Redesign for a Disruptive Training Brand

Brightmoor Labs is a bold, no-fluff sales & leadership training company powered by AI-driven practice and behavioral science. We’ve already built our website structure and copy in Craftly.io — now we need a designer to fully transform the visual design across all pages (Home, Approach, Programs, About, Contact).
We’re looking for a modern, memorable, high-performance aesthetic that blends human energy, science, and tech without feeling corporate or safe. Clean, bold typography, fluid layout, strong emotional hero moments, subtle motion, and imagery that mixes real people with abstract scientific/tech visuals.Because our clients are primarily North American, please ensure any human photography or AI-generated imagery reflects a North American business context and demographics (modern, diverse, and realistic).

Your job is visual redesign only — no coding required.
The final design must be practical to rebuild inside Craftly.io.

A full, detailed creative brief (plus logo files) is included in the uploaded files.
If you can bring a mix of edge, intelligence, and strong visual storytelling, we’d love to see your work.

Website is already built in Craftly.io at - https://brightmoor-website-tempdesign.craftly.app — structure is set, visuals need redesign.

```html
<!DOCTYPE html>
<html lang="en">
<head>
<meta charset="utf-8">
<title>Brightmoor Labs — Training that practices back</title>
<link href="https://fonts.googleapis.com/css2?family=Open+Sans:wght@400;500;600;700&display=swap" rel="stylesheet">
<style>
:root{
  --navy:#0c1c44;
  --navy-deep:#0a1634;
  --blue:#3d63b6;
  --blue-head:#3a62b8;
  --blue-mid:#2f6fc7;
  --hero-a:#1b4fa8;
  --hero-b:#2f8ad8;
  --sky:#dff1fb;
  --cyan:#7fd3f4;
  --cyan-soft:#bfe9fa;
  --ink:#1b1f2a;
  --muted:#4a5060;
  --white:#ffffff;
}
*{box-sizing:border-box;margin:0;padding:0}
html,body{width:1200px;height:4129px;overflow:hidden}
body{font-family:"Open Sans",Arial,sans-serif;color:var(--ink);background:var(--white)}
section,footer{position:relative;width:1200px;overflow:hidden}
.abs{position:absolute}
.center{text-align:center;left:0;right:0}
.btn{position:absolute;display:flex;align-items:center;justify-content:center;gap:12px;font-size:12px;font-weight:600;letter-spacing:.3px;text-transform:uppercase;height:39px}
.btn svg{width:14px;height:14px}
.btn-dark{background:var(--navy);color:var(--white)}
.btn-light{background:var(--white);color:var(--navy)}
.btn-ghost{border:1.5px solid rgba(255,255,255,.85);color:var(--white)}
.h2{font-size:31px;font-weight:500;color:var(--ink)}
.h2 b{font-weight:600;color:var(--blue-head)}

/* hero */
.hero{height:660px;background:var(--white)}
.hero-bg{position:absolute;inset:0}
.nav{position:absolute;left:125px;right:125px;top:0;height:68px;border-bottom:1px solid rgba(255,255,255,.55)}
.brand{position:absolute;left:4px;top:22px;display:flex;align-items:center;gap:8px;color:var(--white);font-size:13px;font-weight:700;letter-spacing:1px}
.brand i{width:14px;height:14px;background:var(--white);display:block}
.nav-links{position:absolute;left:409px;top:28px;display:flex;gap:36px;font-size:12px;font-weight:600;color:var(--white)}
.nav-links .on{border-bottom:1.5px solid var(--white);padding-bottom:3px}
.nav .btn{left:846px;top:20px;width:104px;height:32px;font-size:11px}
.hero-title{top:162px;font-size:62px;font-weight:600;color:var(--white);letter-spacing:-.5px}
.hero-sub{top:244px;font-size:22px;color:var(--white)}
.hero-body{top:284px;font-size:15px;line-height:25px;color:rgba(255,255,255,.92)}

/* problem / solution */
.fix{height:422px}
.fix-box{position:absolute;left:125px;top:16px;width:950px;height:374px;background:var(--blue)}
.fix-col{position:absolute;top:0;width:300px;padding:28px 0 0 31px;color:var(--white)}
.fix-col .ico{width:44px;height:44px;border-radius:50%;background:var(--white);display:flex;align-items:center;justify-content:center}
.fix-col h3{margin-top:18px;font-size:17px;font-weight:500}
.fix-col ul{margin-top:12px;list-style:none}
.fix-col li{font-size:11px;line-height:15px;margin-bottom:13px;padding-left:9px;position:relative;width:260px}
.fix-col li::before{content:"";position:absolute;left:0;top:6px;width:3px;height:3px;border-radius:50%;background:var(--white)}
.fix-card{position:absolute;left:313px;top:11px;width:324px;height:363px;background:var(--white);text-align:center;padding-top:100px}
.fix-card h2{font-size:30px;line-height:38px;font-weight:500}
.fix-card h2 b{color:var(--blue-head);font-weight:600}
.fix-card p{margin:16px auto 0;width:280px;font-size:11px;line-height:17px;color:var(--muted)}

/* measure */
.measure{height:408px;background:var(--sky)}
.stat{position:absolute;top:100px;width:220px;margin-left:-110px;text-align:center}
.stat .dot{width:92px;height:92px;margin:0 auto;border-radius:50%;background:var(--navy);display:flex;align-items:center;justify-content:center}
.stat p{margin-top:22px;font-size:12px;color:var(--ink)}

/* system */
.system{height:454px}
.step{position:absolute;top:74px;width:220px;margin-left:-110px;text-align:center}
.ring{width:152px;height:152px;margin:0 auto;border-radius:50%;background:var(--white);border:2px solid #b8e4f8;box-shadow:0 0 18px rgba(87,190,240,.45);display:flex;align-items:center;justify-content:center}
.step h3{margin-top:17px;font-size:18px;font-weight:500}
.step p{margin-top:6px;font-size:11px;line-height:18px;color:var(--muted)}
.dash{position:absolute}

/* practice */
.practice{height:359px;background:linear-gradient(180deg,#3a5fc0 0%,#3153b6 60%,#3a60c2 100%)}
.practice .h2{color:var(--white)}
.practice .h2 b{color:var(--white)}
.pcard{position:absolute;top:111px;height:176px;background:var(--white);text-align:center;padding-top:34px}
.pcard h3{font-size:17px;font-weight:500}
.pcard hr{border:0;border-top:1px solid #cfd6e6;width:180px;margin:8px auto 0}
.pcard p{margin:12px auto 0;width:255px;font-size:11px;line-height:18px;color:var(--muted)}
.pcard.alt{background:#4d79d4;border:1.5px solid #a9c4f2;color:var(--white)}
.pcard.alt h3{color:var(--white)}
.pcard.alt hr{border-color:#a9c4f2}
.pcard.alt p{color:#e3ebfb}

/* programs */
.programs{height:323px}
.prog-head{left:191px;top:80px;font-size:31px;line-height:40px;font-weight:500}
.prog-head b{color:var(--blue-head);font-weight:600}
.prog-body{left:192px;top:170px;width:290px;font-size:11px;line-height:18px;color:var(--muted)}
.prog-card{position:absolute;left:612px;top:65px;width:398px;height:240px;background:#f4f9fd;border:1.5px solid #bfe5f7;text-align:center;padding-top:38px}
.prog-card .dot{width:72px;height:72px;margin:0 auto;border-radius:50%;background:var(--navy);display:flex;align-items:center;justify-content:center}
.prog-card h3{margin-top:22px;font-size:22px;font-weight:500}
.prog-card p{margin:10px auto 0;width:290px;font-size:10px;line-height:17px;color:var(--muted)}

/* team */
.team{height:331px;background:var(--sky)}
.team p.lead{top:169px;width:760px;margin:0 auto;font-size:11px;line-height:19px;color:var(--muted)}

/* insights */
.insights{height:642px}
.ins-head{top:60px;font-size:31px;line-height:40px;font-weight:500}
.ins-head b{color:var(--blue-head);font-weight:600}
.post{position:absolute;top:159px;width:304px}
.post .media{height:191px}
.post h3{margin-top:30px;font-size:17px;line-height:22px;font-weight:600}
.post p{margin-top:12px;font-size:11px;line-height:19px;color:var(--muted)}
.post small{display:block;margin-top:12px;font-size:10px;color:var(--muted)}

/* cta + footer */
.foot{height:530px;background:linear-gradient(180deg,var(--white) 0,var(--white) 128px,var(--navy-deep) 128px)}
.cta{position:absolute;left:125px;top:1px;width:950px;height:287px;background:linear-gradient(120deg,#2a62c4 0%,#3a80d4 55%,#2b6cc8 100%);text-align:center;color:var(--white)}
.cta h2{margin-top:52px;font-size:30px;font-weight:600}
.cta p{margin:14px auto 0;width:420px;font-size:16px;line-height:26px;color:#e9f1fc}
.fcol{position:absolute;top:300px;color:var(--white)}
.fcol h4{font-size:14px;font-weight:600;margin-bottom:15px}
.fcol p{font-size:11px;line-height:17px;color:#d7deec}
.flinks a{display:block;font-size:11px;color:#d7deec;text-decoration:none;margin-bottom:10px}
.contact-row{display:flex;align-items:flex-start;gap:12px;font-size:11px;line-height:17px;color:#d7deec;margin-bottom:15px}
.contact-row i{flex:none;width:20px;height:20px;border:1.3px solid var(--white);border-radius:50%;display:flex;align-items:center;justify-content:center}
.field{width:175px;height:24px;background:var(--white);margin-top:12px;font-size:10px;color:#9aa1ae;padding:5px 7px}
.sub-btn{margin-top:10px;width:112px;height:28px;background:var(--white);color:var(--navy);font-size:11px;font-weight:700;display:flex;align-items:center;justify-content:center;gap:10px}
.social{display:flex;gap:8px;margin-top:24px}
.social i{width:19px;height:19px;border:1.3px solid var(--white);border-radius:50%;display:block}
.legal{position:absolute;left:125px;right:125px;top:485px;border-top:1px solid #4a5678;padding-top:13px;font-size:11px;color:#cfd6e6;display:flex;justify-content:space-between}
.legal span+span{word-spacing:26px}
</style>
</head>
<body>

<section class="hero">
  <svg class="hero-bg" width="1200" height="660" viewBox="0 0 1200 660" aria-hidden="true">
    <defs>
      <linearGradient id="heroFill" x1="0" y1="0" x2="1" y2="1">
        <stop offset="0" stop-color="#1a4aa2"/>
        <stop offset=".55" stop-color="#2d7fd2"/>
        <stop offset="1" stop-color="#2a66c0"/>
      </linearGradient>
    </defs>
    <rect width="1200" height="660" fill="#fff"/>
    <polygon points="0,0 1200,0 1200,490 0,590" fill="url(#heroFill)"/>
    <polygon points="0,590 1200,490 1200,520 0,650" fill="#bfe9fa"/>
    <polygon points="0,650 1200,520 0,560" fill="#fff" opacity="0"/>
    <polygon points="370,560 1200,490 1200,650" fill="#28407a"/>
    <polygon points="0,590 650,540 0,650" fill="#c9eefc"/>
  </svg>

  <nav class="nav">
    <div class="brand"><i></i>BRIGHTMOOR LABS</div>
    <div class="nav-links"><span class="on">HOME</span><span>APPROACH</span><span>PROGRAMS</span><span>ABOUT</span><span>CONTACT</span></div>
    <div class="btn btn-light">Let's talk <svg viewBox="0 0 14 14"><path d="M2 2l5 5-5 5M7 2l5 5-5 5" fill="none" stroke="currentColor" stroke-width="1.6"/></svg></div>
  </nav>

  <h1 class="abs center hero-title" style="text-align:center">Training that practices back.</h1>
  <p class="abs center hero-sub" style="text-align:center">AI-driven sustainment that builds mastery — so you don't have to.</p>
  <p class="abs center hero-body" style="text-align:center">You'll see measurable growth as your people turn insight into habit<br>— automatically, sustainably, and without extra work for their leaders.</p>
  <div class="btn btn-light" style="left:433px;top:359px;width:187px">See how we do it <svg viewBox="0 0 14 14"><path d="M2 2l5 5-5 5M7 2l5 5-5 5" fill="none" stroke="currentColor" stroke-width="1.6"/></svg></div>
  <div class="btn btn-ghost" style="left:628px;top:359px;width:138px">Let's talk <svg viewBox="0 0 14 14"><path d="M2 2l5 5-5 5M7 2l5 5-5 5" fill="none" stroke="currentColor" stroke-width="1.6"/></svg></div>
</section>

<section class="fix">
  <div class="fix-box">
    <div class="fix-col" style="left:0">
      <div class="ico"><svg width="26" height="26" viewBox="0 0 26 26"><circle cx="13" cy="13" r="10" fill="#0c1c44"/><path d="M8 13h10M13 8v10" stroke="#7fd3f4" stroke-width="2"/></svg></div>
      <h3>Problem</h3>
      <ul>
        <li>Identifies the real root issue: lack of reinforcement after training.</li>
        <li>Removes blame from learners — the system itself is broken.</li>
        <li>States a universal pain point: workshops fade, habits disappear, coaching is inconsistent.</li>
        <li>Short, impactful sentences enhance clarity and storytelling.</li>
        <li>Builds strong alignment with the reader's lived experience.</li>
      </ul>
    </div>
    <div class="fix-card">
      <h2><b>A System Built for</b><br>Real, Lasting Change</h2>
      <p>A simple, honest narrative that reveals what others won't: why traditional training fails, how your method fixes the broken system, and the measurable results teams can expect. give me in points</p>
    </div>
    <div class="fix-col" style="left:637px">
      <div class="ico"><svg width="26" height="26" viewBox="0 0 26 26"><circle cx="13" cy="11" r="7" fill="#0c1c44"/><rect x="10" y="18" width="6" height="4" fill="#0c1c44"/><circle cx="13" cy="11" r="2.5" fill="#7fd3f4"/></svg></div>
      <h3>Solution</h3>
      <ul>
        <li>Directly addresses and fixes the problem introduced earlier.</li>
        <li>Presents your hybrid model: expert instruction + AI practice + micro-coaching + habit loops.</li>
        <li>Demonstrates credibility with behavioral science terminology.</li>
        <li>Shows learning evolves into measurable performance change.</li>
        <li>Reassures buyers that your system continues long after the workshop.</li>
      </ul>
    </div>
  </div>
</section>

<section class="measure">
  <h2 class="abs center h2" style="top:44px;text-align:center"><b>Behavior Change</b> You Can Measure</h2>
  <div class="stat" style="left:231px"><div class="dot"><svg width="40" height="40" viewBox="0 0 40 40"><circle cx="20" cy="14" r="7" fill="none" stroke="#fff" stroke-width="2"/><path d="M17 22h6M8 32h10l8-4" fill="none" stroke="#7fd3f4" stroke-width="2.5"/></svg></div><p>38% more qualified opportunities</p></div>
  <div class="stat" style="left:487px"><div class="dot"><svg width="40" height="40" viewBox="0 0 40 40"><circle cx="22" cy="13" r="6" fill="none" stroke="#fff" stroke-width="2"/><path d="M8 30h10l10-5" fill="none" stroke="#7fd3f4" stroke-width="2.5"/></svg></div><p>4× practice frequency with integrated AI</p></div>
  <div class="stat" style="left:752px"><div class="dot"><svg width="42" height="42" viewBox="0 0 42 42"><circle cx="21" cy="17" r="11" fill="none" stroke="#fff" stroke-width="2" stroke-dasharray="4 3"/><circle cx="21" cy="14" r="3.5" fill="#fff"/><path d="M8 33h11l10-5" fill="none" stroke="#7fd3f4" stroke-width="2.5"/></svg></div><p>90-day retention significantly higher</p></div>
  <div class="stat" style="left:986px"><div class="dot"><svg width="40" height="40" viewBox="0 0 40 40"><rect x="16" y="6" width="12" height="15" fill="#fff"/><path d="M22 6v15" stroke="#0c1c44" stroke-width="1.5"/><path d="M8 30h10l10-5" fill="none" stroke="#7fd3f4" stroke-width="2.5"/></svg></div><p>Quick to Learn, Built to Last</p></div>
  <div class="btn btn-dark" style="left:508px;top:266px;width:183px">See case studies <svg viewBox="0 0 14 14"><path d="M2 2l5 5-5 5M7 2l5 5-5 5" fill="none" stroke="currentColor" stroke-width="1.6"/></svg></div>
  <svg class="abs" style="left:0;top:300px" width="1200" height="108" viewBox="0 0 1200 108" aria-hidden="true">
    <polygon points="0,108 1200,108 1200,70 0,40" fill="#fff"/>
    <polygon points="0,22 0,108 420,50" fill="#9fdcf6"/>
    <polygon points="0,40 1200,70 0,108" fill="#fff"/>
    <polygon points="0,55 260,65 0,108" fill="#8fd7f5"/>
  </svg>
</section>

<section class="system">
  <h2 class="abs center h2" style="top:14px;text-align:center"><b>A System Designed</b> for Lasting Behavior Change</h2>
  <svg class="dash" style="left:310px;top:110px" width="580" height="80" viewBox="0 0 580 80" aria-hidden="true">
    <path d="M2 20 Q35 6 70 14" fill="none" stroke="#0c1c44" stroke-width="2.5" stroke-dasharray="5 5"/><path d="M66 8l8 6-9 4z" fill="#0c1c44"/>
    <path d="M248 68 Q282 74 318 60" fill="none" stroke="#0c1c44" stroke-width="2.5" stroke-dasharray="5 5"/><path d="M314 54l8 5-8 6z" fill="#0c1c44"/>
    <path d="M500 20 Q535 6 570 14" fill="none" stroke="#0c1c44" stroke-width="2.5" stroke-dasharray="5 5"/><path d="M566 8l8 6-9 4z" fill="#0c1c44"/>
  </svg>
  <div class="step" style="left:226px"><div class="ring"><svg width="76" height="60" viewBox="0 0 76 60"><rect x="34" y="22" width="7" height="20" fill="#3a8ee0"/><rect x="45" y="14" width="7" height="28" fill="#3a8ee0"/><rect x="56" y="8" width="7" height="34" fill="#3a8ee0"/><circle cx="22" cy="42" r="13" fill="#0c1c44"/><circle cx="22" cy="42" r="5" fill="#fff"/><path d="M8 28l16-12 12 6 18-14" fill="none" stroke="#0c1c44" stroke-width="2.5"/></svg></div><h3>Diagnose</h3><p>Identify capability gaps, behavioral barriers, and team patterns so training aligns with real performance needs.</p></div>
  <div class="step" style="left:474px"><div class="ring"><svg width="76" height="66" viewBox="0 0 76 66"><rect x="26" y="6" width="40" height="20" rx="3" fill="#5ac0f0"/><rect x="28" y="32" width="18" height="16" fill="#0c1c44"/><path d="M10 56h22l22-10" fill="none" stroke="#3a8ee0" stroke-width="4"/><rect x="10" y="40" width="10" height="18" fill="#0c1c44"/></svg></div><h3>Deliver</h3><p>Run high-impact workshops led by operators who've been in the field — practical, fast, and immediately applicable.</p></div>
  <div class="step" style="left:723px"><div class="ring"><svg width="70" height="66" viewBox="0 0 70 66"><circle cx="35" cy="30" r="9" fill="#3a8ee0"/><path d="M12 20 Q35 70 58 20" fill="none" stroke="#0c1c44" stroke-width="8" stroke-linecap="round"/><circle cx="35" cy="6" r="5" fill="#0c1c44"/><circle cx="14" cy="12" r="5" fill="#0c1c44"/><circle cx="56" cy="12" r="5" fill="#0c1c44"/><path d="M14 12 Q35 -4 56 12" fill="none" stroke="#3a8ee0" stroke-width="2"/></svg></div><h3>Reinforce</h3><p>Keep skills alive with AI practice, micro-coaching, nudges, and habit-building reinforcement that sticks.</p></div>
  <div class="step" style="left:968px"><div class="ring"><svg width="76" height="64" viewBox="0 0 76 64"><rect x="12" y="34" width="9" height="14" fill="#3a8ee0"/><rect x="25" y="26" width="9" height="22" fill="#3a8ee0"/><rect x="38" y="18" width="9" height="30" fill="#3a8ee0"/><rect x="51" y="10" width="9" height="38" fill="#3a8ee0"/><path d="M10 26L50 4" stroke="#0c1c44" stroke-width="2.5"/><path d="M44 2l8 1-3 7" fill="none" stroke="#0c1c44" stroke-width="2.5"/><rect x="6" y="52" width="64" height="8" fill="#0c1c44"/></svg></div><h3>Measure</h3><p>Track progress with skill mastery dashboards, behavioral data, and performance insights that prove ROI.</p></div>
  <div class="btn btn-dark" style="left:500px;top:352px;width:199px">Learn the process <svg viewBox="0 0 14 14"><path d="M2 2l5 5-5 5M7 2l5 5-5 5" fill="none" stroke="currentColor" stroke-width="1.6"/></svg></div>
</section>

<section class="practice">
  <h2 class="abs center h2" style="top:52px;text-align:center"><b>Practice</b> Makes Performance</h2>
  <div class="pcard" style="left:125px;width:296px"><h3>Learn Fast</h3><hr><p>Immersive, expert-led workshops that build skills quickly through role-play, real conversations, and scenario-based practice. Teams leave with confidence, not confusion.</p></div>
  <div class="pcard alt" style="left:454px;width:293px"><h3>Certify</h3><hr><p>Competency is validated through structured assessments, coaching checkpoints, and AI-evaluated simulations that ensure skills meet a consistent standard.</p></div>
  <div class="pcard" style="left:779px;width:296px"><h3>Sustain</h3><hr><p>Daily micro-practice, spaced repetition, nudges, and habit triggers keep skills active long after training day — ensuring behavior sticks for the long term.</p></div>
</section>

<section class="programs">
  <h2 class="abs prog-head"><b>Programs That Transform</b><br>How Teams Perform</h2>
  <p class="abs prog-body">High-impact, modern training experiences designed to build the skills today's teams actually need — and reinforce them until they stick.</p>
  <div class="btn btn-dark" style="left:194px;top:246px;width:237px">Explore all programs <svg viewBox="0 0 14 14"><path d="M2 2l5 5-5 5M7 2l5 5-5 5" fill="none" stroke="currentColor" stroke-width="1.6"/></svg></div>
  <div class="prog-card">
    <div class="dot"><svg width="34" height="34" viewBox="0 0 34 34"><path d="M28 6c-9 0-15 6-18 13l5 5c7-3 13-9 13-18z" fill="#fff"/><circle cx="21" cy="13" r="2.5" fill="#0c1c44"/><path d="M10 19l-4 1 3-6M15 24l-1 4 6-3" fill="#fff"/><path d="M9 25l-3 3" stroke="#7fd3f4" stroke-width="2"/></svg></div>
    <h3>Sales Mastery Accelerator</h3>
    <p>A complete skills transformation for revenue teams. From discovery to objection handling to closing, this program builds confident, consistent, high-performing sellers.</p>
  </div>
</section>

<section class="team">
  <svg class="abs" style="left:0;top:0" width="1200" height="100" viewBox="0 0 1200 100" aria-hidden="true">
    <polygon points="0,0 1200,0 1200,30 0,60" fill="#fff"/>
    <polygon points="0,0 700,60 0,60" fill="#bfe9fa"/>
    <polygon points="1200,30 860,76 1200,100" fill="#7fd3f4"/>
  </svg>
  <h2 class="abs center h2" style="top:117px;text-align:center"><b>Built by People</b> Who've Led the Change Themselves</h2>
  <p class="abs center lead" style="text-align:center">Our facilitators, advisors, and coaches come from the real world — operators who've built, scaled, and led high-performance teams across sales, leadership, and operations. They've experienced the same challenges your organization faces, which is why our approach is practical, realistic, and grounded in human behavior. Everything we teach is field-tested, battle-proven, and designed for real-world results.</p>
  <div class="btn btn-dark" style="left:513px;top:245px;width:173px">Meet the team <svg viewBox="0 0 14 14"><path d="M2 2l5 5-5 5M7 2l5 5-5 5" fill="none" stroke="currentColor" stroke-width="1.6"/></svg></div>
</section>

<section class="insights">
  <h2 class="abs center ins-head" style="text-align:center"><b>Insights From the Front Lines</b><br>of Learning &amp; Performance</h2>
  <article class="post" style="left:125px">
    <div class="media" role="img" aria-label="Photo of a person touching a glowing training interface with learning icons" style="background:linear-gradient(135deg,#0d3a7a,#2a72c8 60%,#143e80)"></div>
    <h3>Why Training Fails —<br>and How to Fix It</h3>
    <p>A breakdown of the structural gaps in traditional training systems — and the reinforcement model organizations need for real, lasting behavior change.</p>
    <small>Oct 12, 2025 · 6 min read</small>
  </article>
  <article class="post" style="left:449px">
    <div class="media" role="img" aria-label="Photo of hands at a laptop beneath a glowing AI circuit graphic" style="background:linear-gradient(135deg,#0b1424,#1d3c66 55%,#0d1a30)"></div>
    <h3>AI Practice: The Future of<br>Skill Reinforcement</h3>
    <p>How AI-driven simulations, micro-coaching, and feedback loops are redefining skill mastery and accelerating performance.</p>
    <small>Sept 28, 2025 · 5 min read</small>
  </article>
  <article class="post" style="left:772px">
    <div class="media" role="img" aria-label="Digital rendering of a glowing brain against a dark data background" style="background:linear-gradient(135deg,#0a1326,#27558e 50%,#3b1e2e)"></div>
    <h3>The Neuroscience of<br>Behavior Change</h3>
    <p>What the brain needs to build, adopt, and retain new habits — grounded in cognitive and behavioral science research.</p>
    <small>Aug 19, 2025 · 7 min read</small>
  </article>
  <div class="btn btn-dark" style="left:518px;top:539px;width:164px">Visit insights <svg viewBox="0 0 14 14"><path d="M2 2l5 5-5 5M7 2l5 5-5 5" fill="none" stroke="currentColor" stroke-width="1.6"/></svg></div>
</section>

<footer class="foot">
  <div class="cta">
    <h2>Ready to Build Training That Actually Sticks?</h2>
    <p>Experience the system designed to create real behavior change — not just another workshop.</p>
    <div class="btn btn-light" style="left:301px;top:157px;width:152px">Get a demo <svg viewBox="0 0 14 14"><path d="M2 2l5 5-5 5M7 2l5 5-5 5" fill="none" stroke="currentColor" stroke-width="1.6"/></svg></div>
    <div class="btn btn-ghost" style="left:458px;top:157px;width:193px">Talk to a specialist <svg viewBox="0 0 14 14"><path d="M2 2l5 5-5 5M7 2l5 5-5 5" fill="none" stroke="currentColor" stroke-width="1.6"/></svg></div>
  </div>

  <div class="fcol" style="left:125px;width:270px">
    <h4 style="font-size:12px;letter-spacing:.5px;display:flex;align-items:center;gap:8px"><i style="width:12px;height:12px;background:#fff;display:block"></i>BRIGHTMOOR LABS</h4>
    <p>This site introduces Brightmoor Labs, a modern learning and performance company built to solve the biggest problem in corporate training: skills don't stick without reinforcement.</p>
    <div class="social"><i></i><i></i></div>
  </div>
  <div class="fcol flinks" style="left:446px">
    <h4>Quick Links</h4>
    <a>Home</a><a>Approach</a><a>Programs</a><a>About</a><a>Contact</a>
  </div>
  <div class="fcol" style="left:638px;width:220px">
    <h4>Get in Touch</h4>
    <div class="contact-row"><i><svg width="10" height="10" viewBox="0 0 10 10"><path d="M2 1l2 2-1 1.5c.6 1.2 1.4 2 2.5 2.5L7 6l2 2-1 1.5C4.5 9 1 5.5.5 2z" fill="#fff"/></svg></i><span>1 (555) 014-2290</span></div>
    <div class="contact-row"><i><svg width="10" height="8" viewBox="0 0 10 8"><rect x=".5" y=".5" width="9" height="7" fill="none" stroke="#fff"/><path d="M.5 .5L5 4.5 9.5.5" fill="none" stroke="#fff"/></svg></i><span>contact@brightmoorlabs.com</span></div>
    <div class="contact-row"><i><svg width="9" height="11" viewBox="0 0 9 11"><path d="M4.5 10.5S1 6.5 1 4.2a3.5 3.5 0 017 0c0 2.3-3.5 6.3-3.5 6.3z" fill="#fff"/><circle cx="4.5" cy="4.2" r="1.3" fill="#0a1634"/></svg></i><span>4820 Larkspur Ave Suite 210<br>Fairview, AZ 85099</span></div>
  </div>
  <div class="fcol" style="left:872px;width:203px">
    <h4>Subscribe Newslatter</h4>
    <p>Join leaders who receive monthly insights on training that actually sticks.</p>
    <div class="field">Email</div>
    <div class="sub-btn">SUBSCRIBE <svg width="12" height="12" viewBox="0 0 14 14"><path d="M2 2l5 5-5 5M7 2l5 5-5 5" fill="none" stroke="currentColor" stroke-width="1.6"/></svg></div>
  </div>

  <div class="legal"><span>© 2024 Brightmoor Labs. All rights reserved.</span><span>Terms Privacy</span></div>
</footer>

</body>
</html>
```